Business cards for Keelstone Consulting (Leadership & Performance Coaching and HR Consulting)

I have a logo (although I'm open to new ideas) and I need this added to a business card. Ultimately, I will also need help with a website. This is an independent consulting firm that is focuses on Leadership, Performance, Executive Coaching and Talent.
Google the story about "one storm, one sailor" ... hence the Keelstone

Target Market(s)

My clients, CEOs, CHROs, COOs

Contact Information for Business Card

Dana K. Wolfe
President
503.553.0871
dwolfe52@ventomail.net
www.KeelstoneConsulting.com
3918 Hollowmere Dr., Larkmoor, OR 97186

Font styles to use
Serif
Sans Serif

Colors
ec1f27
0455a3

Requirements
Must have
• Color, be professional
Nice to have
• Something that pops off the card
Should not have
• Be boring.

```html
<!DOCTYPE html>
<html lang="en">
<head>
<meta charset="utf-8">
<title>Keelstone Consulting – Business Cards</title>
<link rel="stylesheet" href="https://fonts.googleapis.com/css2?family=Roboto:ital,wght@0,400;0,700;1,400;1,700&display=swap">
<style>
  :root {
    --backdrop: #3a3a3c;
    --card: #232325;
    --red: #ec1f27;
    --blue: #0455a3;
    --blue-light: #3f9be6;
    --white: #f2f2f2;
  }
  * { margin: 0; padding: 0; box-sizing: border-box; }
  html, body {
    width: 799px; height: 1200px; overflow: hidden;
    background: var(--backdrop);
    font-family: "Roboto", sans-serif;
  }
  .card {
    position: absolute; left: 70px; width: 660px; height: 380px;
    background: var(--card); border-radius: 28px; overflow: hidden;
    box-shadow: 0 18px 40px rgba(0,0,0,.45);
  }
  .card--front { top: 110px; }
  .card--back { top: 710px; }

  .brand { position: absolute; display: flex; align-items: center; gap: 14px; }
  .brand__dot { border-radius: 50%; background: var(--red); flex: none; }
  .brand__name { color: var(--red); font-weight: 700; white-space: nowrap; }

  .card--front .brand { left: 0; right: 0; top: 124px; justify-content: center; }
  .card--front .brand__dot { width: 44px; height: 44px; }
  .card--front .brand__name { font-size: 42px; }

  .front__web {
    position: absolute; left: 0; right: 0; top: 262px; text-align: center;
    color: var(--white); font-size: 18px; line-height: 22px;
  }
  .front__dash {
    position: absolute; top: 272px; height: 3px; width: 70px; border-radius: 2px;
    background: linear-gradient(90deg, var(--blue), var(--blue-light));
  }
  .front__dash--left { left: 100px; }
  .front__dash--right { right: 100px; }
  .front__band {
    position: absolute; left: 0; right: 0; bottom: 0; height: 9px;
    background: linear-gradient(90deg, var(--blue) 0%, var(--blue-light) 48%, var(--red) 48%, var(--red) 100%);
  }

  .back__tab {
    position: absolute; left: -30px; top: 28px; width: 60px; height: 60px;
    border-radius: 50%; background: linear-gradient(135deg, var(--blue-light), var(--blue));
  }
  .back__person { position: absolute; left: 48px; top: 34px; }
  .back__name { color: var(--red); font-size: 26px; font-weight: 700; font-style: italic; }
  .back__title { color: var(--white); font-size: 15px; font-style: italic; margin-top: 2px; }

  .contact { position: absolute; left: 40px; top: 226px; list-style: none; color: var(--white); font-size: 16px; }
  .contact__item { display: flex; align-items: center; gap: 12px; height: 25px; }
  .contact__icon { width: 14px; height: 14px; fill: var(--red); flex: none; }
  .contact__address { margin-top: 2px; margin-left: -10px; }

  .card--back .brand { right: 46px; top: 150px; }
  .card--back .brand__dot { width: 30px; height: 30px; }
  .card--back .brand__name { font-size: 28px; }
</style>
</head>
<body>
  <section class="card card--front">
    <div class="brand">
      <span class="brand__dot"></span>
      <span class="brand__name">Keelstone Consulting</span>
    </div>
    <span class="front__dash front__dash--left"></span>
    <p class="front__web">www.KeelstoneConsulting.com</p>
    <span class="front__dash front__dash--right"></span>
    <div class="front__band"></div>
  </section>

  <section class="card card--back">
    <span class="back__tab"></span>
    <div class="back__person">
      <p class="back__name">Dana K. Wolfe</p>
      <p class="back__title">President</p>
    </div>

    <div class="brand">
      <span class="brand__dot"></span>
      <span class="brand__name">Keelstone Consulting</span>
    </div>

    <ul class="contact">
      <li class="contact__item">
        <svg class="contact__icon" viewBox="0 0 24 24" aria-hidden="true"><path d="M6.6 10.8a15 15 0 0 0 6.6 6.6l2.2-2.2a1 1 0 0 1 1-.25 11.4 11.4 0 0 0 3.6.57 1 1 0 0 1 1 1V20a1 1 0 0 1-1 1A17 17 0 0 1 3 4a1 1 0 0 1 1-1h3.5a1 1 0 0 1 1 1c0 1.25.2 2.45.57 3.57a1 1 0 0 1-.25 1z"/></svg>
        503.553.0871
      </li>
      <li class="contact__item">
        <svg class="contact__icon" viewBox="0 0 24 24" aria-hidden="true"><path d="M2 5h20v14H2z M4 7v.4l8 5 8-5V7l-8 5z" fill-rule="evenodd"/></svg>
        dwolfe52@ventomail.net
      </li>
      <li class="contact__item">
        <svg class="contact__icon" viewBox="0 0 24 24" aria-hidden="true"><circle cx="12" cy="12" r="10"/><path d="M2 12h20M12 2c3 3 3 17 0 20M12 2c-3 3-3 17 0 20" stroke="#232325" stroke-width="1.5" fill="none"/></svg>
        www.KeelstoneConsulting.com
      </li>
      <li class="contact__item contact__address">3918 Hollowmere Dr., Larkmoor, OR 97186</li>
    </ul>
  </section>
</body>
</html>
```